Tovaro Digital LinkedIn Page and Twitter Account

We are an advanced technology company focused on government technologies like e-Health, e-Finance, Digital Identity and Data Intelligence. We want to launch our LinkedIn and Twitter pages and we need to design all the infographics and banners to launch the campaign.

The agency/freelancer needs to go through all the products and services to digest the business very well in order to build a creative designs and content.

Our website is: www.tovarodigital.example

```html
<!DOCTYPE html>
<html lang="en">
<head>
<meta charset="utf-8">
<title>Tovaro Digital – Banner</title>
<link href="https://fonts.googleapis.com/css2?family=Montserrat:wght@500;600;700&display=swap" rel="stylesheet">
<style>
  :root {
    --teal-deep: #17767e;
    --teal-mid: #2596a0;
    --teal-bright: #3fb3b5;
    --teal-pale: #a9d8d8;
    --teal-mist: #d6ecec;
    --white: #ffffff;
    --icon: #f2fafa;
  }
  * { box-sizing: border-box; margin: 0; padding: 0; }
  html, body { width: 1200px; height: 400px; overflow: hidden; background: var(--teal-mid); }
  body { font-family: "Montserrat", Arial, sans-serif; color: var(--white); }

  .banner { position: relative; width: 1200px; height: 400px; overflow: hidden; }

  .backdrop-photo {
    position: absolute; inset: 0;
    background:
      radial-gradient(ellipse 320px 260px at 520px 180px, rgba(255,255,255,0.10), transparent 70%),
      linear-gradient(90deg, var(--teal-bright) 0%, var(--teal-mid) 35%, var(--teal-deep) 55%, #2a8f96 70%, var(--teal-pale) 100%);
  }
  .office-photo {
    position: absolute; top: 0; right: 0; width: 560px; height: 400px;
    clip-path: polygon(38% 0, 100% 0, 100% 100%, 0 100%);
    background: linear-gradient(100deg, rgba(120,196,198,0.55) 0%, var(--teal-pale) 40%, var(--teal-mist) 75%, #bfe0e0 100%);
  }

  .brand { position: absolute; left: 40px; top: 34px; display: flex; align-items: center; gap: 12px; }
  .brand-dot { width: 34px; height: 34px; border-radius: 50%; background: var(--white); }
  .brand-name { font-size: 28px; font-weight: 500; line-height: 28px; letter-spacing: 0.5px; color: var(--white); }
  .brand-rule { position: absolute; left: 40px; top: 114px; width: 160px; height: 2px; background: var(--white); }

  .headline {
    position: absolute; left: 38px; top: 138px;
    font-size: 38px; font-weight: 700; line-height: 48px; letter-spacing: 0.2px;
  }

  .tagline {
    position: absolute; left: 38px; top: 292px;
    font-size: 13.5px; font-weight: 600; line-height: 24px;
  }

  .services { position: absolute; left: 647px; top: 44px; width: 252px; display: grid; grid-template-columns: 126px 126px; row-gap: 14px; }
  .service { display: flex; flex-direction: column; align-items: center; text-align: center; }
  .service.row-three { margin-top: 6px; }
  .service svg { width: 52px; height: 48px; margin-bottom: 6px; }
  .service-label { font-size: 14px; font-weight: 600; line-height: 17.5px; }
</style>
</head>
<body>
<main class="banner">
  <div class="backdrop-photo" role="img" aria-label="Teal-toned photo of hands typing on a laptop, overlaid with a soft dotted wave"></div>
  <div class="office-photo" role="img" aria-label="Teal-toned photo of two colleagues reviewing charts at a desk in a bright office"></div>

  <div class="brand">
    <span class="brand-dot"></span>
    <span class="brand-name">tovaro<br>digital</span>
  </div>
  <div class="brand-rule"></div>

  <h1 class="headline">
    Digital with<br>
    customer experience<br>
    at the core
  </h1>

  <p class="tagline">
    Engineering digital platforms that scales with economy and rich in data.<br>
    Architecting with putting customer journey in the center.
  </p>

  <section class="services">
    <div class="service">
      <svg viewBox="0 0 52 48" aria-hidden="true"><rect x="4" y="6" width="44" height="30" rx="2" fill="none" stroke="var(--icon)" stroke-width="2"/><path d="M16 16h6l12-6v20l-12-6h-6z" fill="var(--icon)"/><rect x="2" y="38" width="48" height="4" fill="var(--icon)"/></svg>
      <span class="service-label">Digital<br>Government</span>
    </div>
    <div class="service">
      <svg viewBox="0 0 52 48" aria-hidden="true"><path d="M10 40L34 16" stroke="var(--icon)" stroke-width="5" stroke-linecap="round"/><path d="M42 40L18 16" stroke="var(--icon)" stroke-width="5" stroke-linecap="round"/><circle cx="38" cy="11" r="7" fill="none" stroke="var(--icon)" stroke-width="4"/><rect x="9" y="5" width="12" height="10" fill="var(--icon)"/></svg>
      <span class="service-label">IT Reforms</span>
    </div>
    <div class="service">
      <svg viewBox="0 0 52 48" aria-hidden="true"><rect x="4" y="4" width="44" height="30" rx="2" fill="var(--icon)"/><path d="M12 12h4M20 12h18M12 19h4M20 19h14M12 26h4M20 26h18" stroke="var(--teal-mid)" stroke-width="2.5"/><rect x="22" y="34" width="8" height="6" fill="var(--icon)"/><rect x="14" y="40" width="24" height="3" fill="var(--icon)"/></svg>
      <span class="service-label">Software<br>Developments</span>
    </div>
    <div class="service">
      <svg viewBox="0 0 52 48" aria-hidden="true"><circle cx="18" cy="11" r="7" fill="var(--icon)"/><path d="M6 44V28c0-6 5-9 12-9s12 3 12 9v16z" fill="var(--icon)"/><circle cx="36" cy="32" r="9" fill="none" stroke="var(--icon)" stroke-width="5" stroke-dasharray="4 3"/><circle cx="36" cy="32" r="4" fill="var(--icon)"/></svg>
      <span class="service-label">Professional<br>Services</span>
    </div>
    <div class="service row-three">
      <svg viewBox="0 0 52 48" aria-hidden="true"><rect x="4" y="10" width="44" height="34" fill="none" stroke="var(--icon)" stroke-width="2.5"/><path d="M12 10V4M22 10V2M32 10V4M42 10V6M14 20v18M24 22h12M30 22v16M18 30h10" stroke="var(--icon)" stroke-width="2.5"/></svg>
      <span class="service-label">Technology<br>Architectures</span>
    </div>
    <div class="service row-three">
      <svg viewBox="0 0 52 48" aria-hidden="true"><rect x="16" y="2" width="18" height="14" fill="var(--icon)"/><path d="M4 24l10-6h10l6 4 8-4h10v14l-10 8H20L4 34z" fill="var(--icon)"/><path d="M18 28l8 6M24 26l8 6" stroke="var(--teal-mid)" stroke-width="2"/></svg>
      <span class="service-label">Digital Public<br>and Private<br>Partnership</span>
    </div>
  </section>
</main>
</body>
</html>
```